◆コンセプト・特徴

<コンセプト>
シンプルメニューから派手めなメニューまで
お客様に喜んで頂けますようカラー、パーツなど豊富にご用意しております

<特徴>
・モノトーン調の空間
⇒モノトーンを基調としており、
くつろいでいただけるような空間づくりをおこなっております。
・こだわりのスカルプをおこないたい方に満足いただける技術提供
⇒スカルプを得意としており、お好きなデザインにも対応しております。
・スカルプ乗せ放題のプラン
⇒デザインスカルプで且つ乗せ放題のプランがお客様にリーズナブルとご好評いただいております。
・1日4名の限定サロン
⇒一人ひとりのお客様にくつろいで受けていただくため
限定4名とさせていただいております。
完全予約制のため待ち時間なく受けて頂けます。

◆現在のサイトの問題点は?

1デザイン性
2更新の利便性

◆誰向けに発信するサイトなのか

新規顧客向け
ターゲット層:30~40代女性の主婦やお子さん連れの方

◆サイトマップ
1 TOP
2 コンセプト
3 はじめての方へ
4 スタッフ一覧
5 MENU・料金一覧
6 サロン情報
7 当ネイルサロンが選ばれる理由
8 当ネイルサロンのスカルプ
9 問い合わせフォーム
10 リクルート
11 Q&A
12 キャンペーン(一覧)
13 キャンペーン(詳細)
14 ブログ(一覧)
15 ブログ(詳細)
16 ニュース(一覧)
17 ニュース(詳細)
18 ボイス(一覧)
19 ボイス(詳細)

◆デザインのテイスト
希望するイメージ
・シック
・エレガント
・幻想的
ルヴェットやミルダーヌなど黒を基調とした
ブティックの雰囲気のテイストが希望です。

◆希望デザインカラー
モノトーン系(ダークグレージュ)・紫系(店内の色合いと併せてくつろげるようなシックな色合い)

◆参考サイトURL:
色合いやデザインテイストはこの雰囲気が好きです。
こちらにブティックの雰囲気を付け足して下さい。
http://plume-esthe.jp/ 色味などはこのサイトも好きです。

色合いは白っぽいのでNGですが、レイアウトの配置やデザインが好きです。
http://www.tova-nails-co.jp/

◆ワイヤーフレームURL:
https://proto.mockvela.com/view/7c3a1d92-b58e-4f06-9d2a-81e4c0f7a3b5-2d9f/
ワイヤーフレームを用意いたしましたが、素人が作ったものなのでレイアウトの変更などは是非行って頂き、素敵なデザインをご提案頂きたいです。
その際ワイヤーフレーム内のコンテンツは省かず反映いただけますと幸いです。

※可能な限り【ダミー文章】がないよう、
現行サイトの情報よりテキストは反映していただけると助かります。
ご協力の程よろしくお願いいたします。
サイトURL
http://nailsalon-velmira.com/
ページ数
1ページ
希望イメージ
シンプル 複雑
単色 カラフル
暗い 明るい
日常 高級
遊び心 厳粛
未来的 伝統的
女性的 男性的
希望する色
グレー系、紫系
納品ファイル
• フォトショップ形式 (.psd)
• PNG形式 (.png)
補足説明
◆素材について
①素材として必要なものがある場合には、pixora stock画像をご使用ください。
その際、定期契約でダウンロード出来る画像のみを使用してください。
(画像検索した際に出てくる、サムネール下の画像番号の横に
pixoraのマークがあるものは使用しないようお願いいたします)
pixora以外の素材を使用する際には、
必ず無料で提供いただける物のみご使用ください。

②サロンの写真・サイトマップについて
枚数がありますので、下記よりダウンロードしてご使用ください。
https://filevaulto.jp/download/8e1f4a7c93d0b25e6a1c7f04d9b3e82a5c61f0d7
ダウンロードパスワード 9plomk3r
既存サイト内の素材や内容を使用頂いても問題ありません。
素敵なデザインが沢山集まっていますが、もう少し見てから選定したいため延長いたします。
沢山ご応募いただきありがとうございます。
GW中に選定候補の方を検討できたらと考えておりますので
それまで延長を致します。

仮に修正される際は再投稿いただきましたら最新のもので
確認點せていただきます

引き続きよろしくお願いいたします。

黒の割合や差し色などが好みだったため、
今回こちらのデザイナーズ様に選定させて頂きました。

正直どれも素敵だったのですが、
また機会がございましたら宜しくお願いいたします。
今後の皆さまの活躍を応援しております。

```html
<!DOCTYPE html>
<html lang="ja">
<head>
<meta charset="utf-8">
<title>NAIL SALON VELMIRA</title>
<link rel="stylesheet" href="https://fonts.googleapis.com/css2?family=Cormorant+Garamond:wght@400;500;600&family=Noto+Serif+JP:wght@400;500&display=swap">
<style>
:root{
  --ink:#0c0c0c;
  --charcoal:#262424;
  --graphite:#2f2d2d;
  --line:#bdbdbd;
  --paper:#ffffff;
  --soft:#d8d6d6;
  --accent:#9a3fa3;
  --accent-deep:#5c2168;
  --muted:#9b9898;
}
*{box-sizing:border-box;margin:0;padding:0}
html,body{width:1200px;height:5000px;overflow:hidden;background:var(--ink)}
body{font-family:"Noto Serif JP",serif;color:var(--paper);position:relative}
.section{position:absolute;left:0;width:1200px}
.fill{position:absolute;display:block}
.label-en{font-family:"Cormorant Garamond",serif}

/* header */
.hero{top:0;height:690px;background:#161314}
.hero .fill.photo{left:0;top:0;width:1200px;height:690px;background:linear-gradient(100deg,#3a1e2a 0%,#b56a7a 22%,#d8a4a8 38%,#7a2a4c 52%,#1a1416 72%,#0f0d0e 100%)}
.header-brand{position:absolute;left:228px;top:8px;font-family:"Cormorant Garamond",serif;letter-spacing:2px;text-align:center;line-height:1.1}
.header-brand small{display:block;font-size:11px}
.header-brand strong{display:block;font-size:20px;font-weight:500}
.nav{position:absolute;top:62px;left:250px;display:flex;gap:16px;font-family:"Cormorant Garamond",serif;font-size:19px;letter-spacing:1px;white-space:nowrap}
.contact-top{position:absolute;right:72px;top:6px;text-align:right;font-size:15px;line-height:22px;white-space:nowrap}
.sns{display:flex;gap:8px;justify-content:flex-end;margin-bottom:6px}
.sns span{width:24px;height:24px;background:var(--paper);display:block}
.reserve-tab{position:absolute;right:0;top:0;width:56px;height:200px;background:var(--paper);color:var(--ink);writing-mode:vertical-rl;font-size:20px;display:flex;align-items:center;justify-content:center;letter-spacing:4px}
.hero-copy{position:absolute;right:56px;top:250px;width:430px;background:rgba(8,8,8,.55);padding:26px 30px;font-size:15px;line-height:28px;letter-spacing:1px}
.hero-copy h1{font-weight:400;font-size:22px;letter-spacing:4px;margin:-90px 0 60px 40px}
.brand{position:absolute;text-align:center;font-family:"Cormorant Garamond",serif;letter-spacing:3px}
.brand .dot{width:34px;height:34px;border-radius:50%;background:var(--paper);margin:0 auto 8px}
.brand small{display:block;font-size:14px}
.brand strong{display:block;font-weight:500;font-size:26px}

/* section heading */
.heading{position:absolute;left:0;width:1200px;text-align:center;font-family:"Cormorant Garamond",serif;font-size:52px;letter-spacing:8px;font-weight:500}
.heading em{font-style:normal;color:var(--accent)}
.heading .amp{font-size:34px}
.heading-rule{position:absolute;left:400px;width:400px;height:12px}
.more{position:absolute;font-family:"Cormorant Garamond",serif;font-style:italic;font-size:18px;width:120px;height:14px}
.more svg{position:absolute;left:0;top:14px}

/* reason & scalp */
.reason{top:690px;height:930px;background:var(--charcoal)}
.tag{position:absolute;padding:10px 26px;background:#4a4747;font-family:"Cormorant Garamond",serif;font-size:30px;letter-spacing:3px;border:1px solid #6a6666}
.body-text{position:absolute;font-size:14px;line-height:28px;color:var(--soft)}

/* menu */
.menu{top:1620px;height:680px;background:var(--charcoal)}
.menu-row{position:absolute;top:280px;left:148px;width:904px;height:340px;display:flex}
.menu-card{flex:1;position:relative}
.menu-card .fill{left:0;top:0;width:100%;height:100%}
.menu-card p{position:absolute;bottom:0;left:0;right:0;padding:8px;font-size:17px;font-family:"Cormorant Garamond",serif;text-align:center;background:rgba(20,20,20,.7)}
.menu-index{background:var(--ink);display:flex;flex-direction:column;align-items:center;justify-content:center;font-size:16px;gap:6px}

/* ranking */
.ranking{top:2300px;height:800px;background:var(--ink)}
.rank-photo{position:absolute;top:320px;width:244px;height:244px}

/* blog */
.blog{top:3100px;height:690px;background:var(--graphite)}
.post{position:absolute;top:232px;width:206px}
.post .fill{position:relative;width:206px;height:168px}
.post p{font-size:14px;line-height:22px;margin-top:10px}

/* instagram */
.insta{top:3790px;height:590px;background:var(--ink)}
.insta-grid{position:absolute;left:228px;top:160px;width:744px;height:410px}
.insta-mark{position:absolute;left:574px;top:339px;width:52px;height:52px;border:3px solid var(--paper);border-radius:12px;background:rgba(0,0,0,.35)}

/* access */
.access{top:4380px;height:340px}
.address{position:absolute;left:0;top:40px;width:560px;height:200px;background:rgba(255,255,255,.92);color:var(--ink);padding:34px 40px;font-size:16px;line-height:40px}
.pin{display:inline-block;vertical-align:middle;margin-right:6px}

/* footer */
.footer{top:4720px;height:280px;background:var(--ink)}
.foot-contact{position:absolute;left:170px;top:180px;font-size:16px;line-height:26px}
.foot-reserve{position:absolute;left:400px;top:70px;width:130px;height:48px;border:1px solid var(--paper);background:var(--paper);color:var(--ink);text-align:center;line-height:46px;font-size:18px}
.foot-sns{position:absolute;left:410px;top:140px;display:flex;gap:10px}
.foot-sns span{width:28px;height:28px;background:var(--paper)}
.foot-links{position:absolute;top:60px;font-size:14px;line-height:22px;list-style:none}
.foot-divider{position:absolute;left:600px;top:60px;width:1px;height:160px;background:#666}
.copyright{position:absolute;right:30px;bottom:14px;font-size:12px;color:var(--muted)}
</style>
</head>
<body>

<header class="section hero">
  <div class="fill photo" role="img" aria-label="鮮やかなマゼンタのネイルと口元を寄せたビューティービジュアル"></div>
  <div class="header-brand"><small>NAIL SALON</small><strong>VELMIRA</strong></div>
  <nav class="nav"><span>SALON</span><span>CONCEPT</span><span>REASON</span><span>FIRST</span><span>SCALP</span><span>VOICE</span><span>CAMMAIGN</span><span>Q&amp;A</span></nav>
  <div class="contact-top">
    <div class="sns"><span></span><span></span><span></span></div>
    <div>&#9742; 06-4820-1937</div>
    <div>&#9719; 10:00~20:00</div>
  </div>
  <div class="reserve-tab">web予約</div>
  <div class="hero-copy">
    <h1>あなたの指先を華やかに</h1>
    <p>VELMIRA（ヴェルミラ）とはイタリア語で"心"を意味します<br>当店はスカルプやカラー、パーツを豊富に取り揃えております<br>シンプルなメニューから派手めなメニューまで<br>お客様の要望に幅広くお答えいたします</p>
    <p style="margin-top:20px">爪に優しいフィルインの施術も行っております<br>ダメージを最小限にさらに美しく仕上げます</p>
  </div>
  <div class="brand" style="left:850px;top:560px;width:180px">
    <div class="dot"></div><small>NAIL SALON</small><strong>VELMIRA</strong>
  </div>
</header>

<section class="section reason">
  <h2 class="heading" style="top:50px">R<em>E</em>ASON <span class="amp">&amp;</span> SCA<em>L</em>P</h2>
  <svg class="heading-rule" style="top:122px" viewBox="0 0 400 12"><line x1="0" y1="6" x2="392" y2="6" stroke="#bdbdbd" stroke-width="1.5"/><path d="M392 2 L400 6 L392 10" fill="#bdbdbd"/></svg>

  <div class="fill" style="left:108px;top:210px;width:332px;height:260px;background:linear-gradient(135deg,#4a3a30,#8a6e58 45%,#2e2622)" role="img" aria-label="モノトーンを基調とした落ち着いたサロン店内"></div>
  <div class="tag" style="left:800px;top:250px">REASON</div>
  <p class="body-text" style="left:600px;top:330px;width:420px">当店のネイルを選ぶ理由をご紹介いたします。<br>こだわりのシンプルメニューから派手めなメニューまで<br>お客様に喜んで頂けますようカラーやパーツを<br>豊富にご用意しております。</p>
  <div class="more" style="left:1020px;top:492px">more<svg width="120" height="10" viewBox="0 0 120 10"><line x1="0" y1="5" x2="112" y2="5" stroke="#bdbdbd"/><path d="M112 1 L120 5 L112 9" fill="#bdbdbd"/></svg></div>

  <div class="tag" style="left:250px;top:640px">SCALP</div>
  <p class="body-text" style="left:108px;top:720px;width:460px">当ネイルサロンはスカルプを得意としており、<br>一人ひとりのお客様に合わせた長さや形をご提案いたします<br>お好きなデザインにも対応し、乗せ放題のプランも<br>ございますのでお気軽にご相談ください。</p>
  <div class="more" style="left:470px;top:880px">more<svg width="120" height="10" viewBox="0 0 120 10"><line x1="0" y1="5" x2="112" y2="5" stroke="#bdbdbd"/><path d="M112 1 L120 5 L112 9" fill="#bdbdbd"/></svg></div>
  <div class="fill" style="left:688px;top:610px;width:292px;height:280px;background:linear-gradient(140deg,#e6d8e6,#8e4c9a 45%,#c59ac8 75%,#f0e6ee)" role="img" aria-label="パープルのストーンを乗せたスカルプネイル"></div>
</section>

<section class="section menu">
  <h2 class="heading" style="top:120px"><em>M</em>ENU</h2>
  <svg class="heading-rule" style="top:192px" viewBox="0 0 400 12"><line x1="0" y1="6" x2="392" y2="6" stroke="#bdbdbd" stroke-width="1.5"/><path d="M392 2 L400 6 L392 10" fill="#bdbdbd"/></svg>
  <div class="menu-row">
    <div class="menu-card"><div class="fill" style="background:linear-gradient(160deg,#f1e7ec,#c98fa8 50%,#e9d7de)" role="img" aria-label="ジェルネイルの施術例"></div><p>Jel Nail</p></div>
    <div class="menu-card"><div class="fill" style="background:linear-gradient(160deg,#e4ecf2,#8fb3c9 50%,#d7dfe6)" role="img" aria-label="スカルプネイルの施術例"></div><p>Scalp Nail</p></div>
    <div class="menu-card menu-index"><span class="label-en" style="font-size:20px">Menu</span><span>一覧</span><svg width="60" height="8" viewBox="0 0 60 8"><line x1="0" y1="4" x2="54" y2="4" stroke="#bdbdbd"/><path d="M54 1 L60 4 L54 7" fill="#bdbdbd"/></svg></div>
    <div class="menu-card"><div class="fill" style="background:linear-gradient(160deg,#f6e6e0,#d9a79a 50%,#f2dcd5)" role="img" aria-label="ネイルオフの施術イメージ"></div><p>Nail Off</p></div>
    <div class="menu-card"><div class="fill" style="background:linear-gradient(160deg,#f7eef0,#e6b9c4 50%,#faf3f4)" role="img" aria-label="その他メニューのイメージ"></div><p>Other</p></div>
  </div>
</section>

<section class="section ranking">
  <h2 class="heading" style="top:120px">RA<em>N</em>KING <span class="amp">&amp;</span> GAL<em>L</em>ERY</h2>
  <svg class="heading-rule" style="top:192px" viewBox="0 0 400 12"><line x1="0" y1="6" x2="392" y2="6" stroke="#bdbdbd" stroke-width="1.5"/><path d="M392 2 L400 6 L392 10" fill="#bdbdbd"/></svg>
  <div class="fill rank-photo" style="left:192px;background:linear-gradient(150deg,#e9eef2,#a9b6c2 55%,#f3f3f5)" role="img" aria-label="ランキング1位のネイルデザイン"></div>
  <div class="fill rank-photo" style="left:480px;background:linear-gradient(150deg,#f8e9ee,#e0a6ba 55%,#fbf2f4)" role="img" aria-label="ランキング2位のネイルデザイン"></div>
  <div class="fill rank-photo" style="left:760px;background:linear-gradient(150deg,#f6e4ea,#d58ca4 55%,#f4dbe3)" role="img" aria-label="ランキング3位のネイルデザイン"></div>
  <div class="more" style="left:380px;top:640px">next ranking<svg width="140" height="10" viewBox="0 0 140 10"><line x1="0" y1="5" x2="132" y2="5" stroke="#bdbdbd"/><path d="M132 1 L140 5 L132 9" fill="#bdbdbd"/></svg></div>
  <div class="more" style="left:680px;top:640px">gallery<svg width="140" height="10" viewBox="0 0 140 10"><line x1="0" y1="5" x2="132" y2="5" stroke="#bdbdbd"/><path d="M132 1 L140 5 L132 9" fill="#bdbdbd"/></svg></div>
</section>

<section class="section blog">
  <h2 class="heading" style="top:50px">O<em>F</em>FICIAL BLOG</h2>
  <svg class="heading-rule" style="top:122px" viewBox="0 0 400 12"><line x1="0" y1="6" x2="392" y2="6" stroke="#bdbdbd" stroke-width="1.5"/><path d="M392 2 L400 6 L392 10" fill="#bdbdbd"/></svg>
  <article class="post" style="left:160px"><div class="fill" style="background:linear-gradient(140deg,#cfe0ef,#6d9cc6 55%,#e8eef4)" role="img" aria-label="ブログ記事のサムネイル"></div><p>2020.12.12<br>新作デザインのお知らせ…</p></article>
  <article class="post" style="left:395px"><div class="fill" style="background:linear-gradient(140deg,#f3e6df,#cfa795 55%,#f5ece8)" role="img" aria-label="ブログ記事のサムネイル"></div><p>2020.12.12<br>冬のおすすめカラー…</p></article>
  <article class="post" style="left:630px"><div class="fill" style="background:linear-gradient(140deg,#f1e7f1,#c9a3cc 55%,#e9dde9)" role="img" aria-label="ブログ記事のサムネイル"></div><p>2020.12.12<br>雨の日でも華やかに…</p></article>
  <article class="post" style="left:865px"><div class="fill" style="background:linear-gradient(140deg,#f7d86e,#e2578a 50%,#5fb0d6)" role="img" aria-label="ブログ記事のサムネイル"></div><p>2020.12.12<br>いつもと違うスタイル…</p></article>
  <div class="more" style="left:560px;top:586px">next blog<svg width="120" height="10" viewBox="0 0 120 10"><line x1="0" y1="5" x2="112" y2="5" stroke="#bdbdbd"/><path d="M112 1 L120 5 L112 9" fill="#bdbdbd"/></svg></div>
</section>

<section class="section insta">
  <h2 class="heading" style="top:50px">INSTA<em>G</em>LAM</h2>
  <svg class="heading-rule" style="top:122px" viewBox="0 0 400 12"><line x1="0" y1="6" x2="392" y2="6" stroke="#bdbdbd" stroke-width="1.5"/><path d="M392 2 L400 6 L392 10" fill="#bdbdbd"/></svg>
  <div class="fill insta-grid" style="background:linear-gradient(120deg,#c9b8c4,#e58aa6 30%,#8d6fa0 55%,#e9c4cc 80%,#c74a6c)" role="img" aria-label="サロンのネイル作品を並べたギャラリー"></div>
  <div class="insta-mark"></div>
</section>

<section class="section access">
  <div class="fill" style="left:0;top:0;width:1200px;height:340px;background:linear-gradient(180deg,#e6e4e2,#d6d4d2)" role="img" aria-label="サロン周辺の地図"></div>
  <div class="address">
    <div><svg class="pin" width="16" height="22" viewBox="0 0 16 22"><path d="M8 0C3.6 0 0 3.5 0 7.9 0 13.8 8 22 8 22s8-8.2 8-14.1C16 3.5 12.4 0 8 0z" fill="#5c2168"/><circle cx="8" cy="8" r="3" fill="#fff"/></svg>〒530-0099 大阪府大阪市北区白砂町3-8-21</div>
    <div><svg class="pin" width="16" height="16" viewBox="0 0 16 16"><rect x="1" y="1" width="14" height="14" fill="none" stroke="#0c0c0c"/></svg>北白砂駅から徒歩5分</div>
  </div>
  <svg style="position:absolute;left:810px;top:120px" width="28" height="38" viewBox="0 0 16 22"><path d="M8 0C3.6 0 0 3.5 0 7.9 0 13.8 8 22 8 22s8-8.2 8-14.1C16 3.5 12.4 0 8 0z" fill="#5c2168"/><circle cx="8" cy="8" r="3" fill="#fff"/></svg>
</section>

<footer class="section footer">
  <div class="brand" style="left:170px;top:60px;width:140px">
    <div class="dot"></div><small>NAIL SALON</small><strong>VELMIRA</strong>
  </div>
  <div class="foot-contact">&#9742; 06-4820-1937<br>&#9719; 10:00~20:00</div>
  <div class="foot-reserve">web予約</div>
  <div class="foot-sns"><span></span><span></span><span></span></div>
  <div class="foot-divider"></div>
  <ul class="foot-links" style="left:630px">
    <li>TOP</li><li>コンセプト</li><li>はじめての方へ</li><li>スタッフ一覧</li><li>MENU・料金一覧</li><li>サロン情報</li><li>当ネイルサロンが選ばれる理由</li><li>当ネイルサロンのスカルプ</li>
  </ul>
  <ul class="foot-links" style="left:880px">
    <li>問い合わせフォーム</li><li>リクルート</li><li>Q&amp;A</li><li>キャンペーン</li><li>ブログ</li><li>ニュース</li><li>ボイス</li>
  </ul>
  <p class="copyright">Copyright © VELMIRA All Rights reserved.</p>
</footer>

</body>
</html>
```